Design cd cover for the vocal group: Ember, cd title Harbor Light. Cd cover is for EP release to be followed by full album. Songs are: Sizwe Langa Khona(Lift high the lamp); Cold River Road; Ngolwazi(Guide me through the night); When Rain Falls. There is no track entitled harbor light; the concept of the sound of gospel music as embodied in the music tracks - contemporary and traditional - is the basis of the album title.
NB: Project can close Tuesday 12 November to account for the 5 days as I do not count Saturday as a working day.
Hey guys,
Hello to everyone. I would like to take this opportunity to say thank you for your participation. Your submissions have been great and much appreciated. Forgive me for not being able to provide feedback to all of you. The time has come for me to make selection decisions and I would like to say thank you to all for your participation, you have been great and amazing.

```html
<!DOCTYPE html>
<html lang="en">
<head>
<meta charset="utf-8">
<title>Harbor Light – EP Back Cover</title>
<link rel="stylesheet" href="https://fonts.googleapis.com/css2?family=Italiana&family=Marcellus&family=Cormorant+Garamond:wght@400&display=swap">
<style>
  :root {
    --night-deep: #0a0f24;
    --night-mid: #0c2236;
    --night-teal: #0f3a4c;
    --panel-fill: rgba(22, 88, 104, 0.42);
    --ink-light: #f4f2ee;
    --ink-soft: #d9dde2;
    --text-shadow: rgba(0, 0, 0, 0.85);
  }
  * { margin: 0; padding: 0; box-sizing: border-box; }
  html, body {
    width: 1200px;
    height: 1200px;
    overflow: hidden;
    background: var(--night-deep);
  }
  .cover {
    position: relative;
    width: 1200px;
    height: 1200px;
    overflow: hidden;
  }
  .cover-backdrop {
    position: absolute;
    inset: 0;
    width: 1200px;
    height: 1200px;
  }
  .album-title {
    position: absolute;
    left: 890px;
    top: 84px;
    width: 240px;
    font-family: "Italiana", serif;
    font-weight: 400;
    color: var(--ink-light);
    line-height: 108px;
  }
  .album-title .title-line {
    display: block;
    font-size: 86px;
    letter-spacing: -2px;
    white-space: nowrap;
  }
  .album-title .title-line--second {
    margin-left: 30px;
  }
  .album-tagline {
    position: absolute;
    left: 895px;
    top: 317px;
    font-family: "Cormorant Garamond", serif;
    font-size: 16px;
    color: var(--ink-soft);
    letter-spacing: 0.3px;
    white-space: nowrap;
  }
  .tracklist-panel {
    position: absolute;
    left: 130px;
    top: 462px;
    width: 942px;
    height: 276px;
    background: var(--panel-fill);
  }
  .tracklist {
    list-style: none;
    position: absolute;
    left: 216px;
    top: 482px;
    font-family: "Marcellus", serif;
    font-size: 41px;
    color: var(--ink-light);
    text-shadow: 2px 2px 2px var(--text-shadow);
    letter-spacing: 0.3px;
  }
  .tracklist .track {
    height: 59px;
    line-height: 59px;
    white-space: nowrap;
  }
  .track-number { margin-right: 10px; }
</style>
</head>
<body>
  <main class="cover">
    <svg class="cover-backdrop" viewBox="0 0 1200 1200" role="img" aria-label="Dark navy and teal faceted crystal pattern with scattered tiny blue stars">
      <defs>
        <linearGradient id="nightGlow" x1="0" y1="0" x2="1" y2="1">
          <stop offset="0" stop-color="#0b1430"/>
          <stop offset="0.45" stop-color="#0e3246"/>
          <stop offset="0.75" stop-color="#0c2a3e"/>
          <stop offset="1" stop-color="#0a0f26"/>
        </linearGradient>
      </defs>
      <rect width="1200" height="1200" fill="url(#nightGlow)"/>
    </svg>

    <h1 class="album-title">
      <span class="title-line">Harbor</span>
      <span class="title-line title-line--second">Light</span>
    </h1>
    <p class="album-tagline">contemprory and traditional music</p>

    <div class="tracklist-panel"></div>
    <ol class="tracklist">
      <li class="track"><span class="track-number">1.</span> Sizwe Langa Khona(Lift high the lamp)</li>
      <li class="track"><span class="track-number">2.</span>Cold River Road</li>
      <li class="track"><span class="track-number">3.</span>Ngolwazi(Guide me through the night)</li>
      <li class="track"><span class="track-number">4.</span>When Rain Falls</li>
    </ol>
  </main>
</body>
</html>
```